KVR Associates needs a web site

We need a web site for www.kvrassociates-example.com. KVR is a mergers and acquisition consulting company that focuses our buyer and seller services on logistics companies. We help put companies together, and help with legal and financial due diligence. We want the web site to express our service and show the logistics components. We want personalized images versus pictures of trucks and airplanes.

Our new logo uses Burgandy and grey colors. Image attached. We are not in to bold, big letters...classy, artistic, low key preferred. Confidentiality, experience, professional are what we want to express on the site.

All we expect for the first part of this project is a home page, and one subpage.  We are budgeting other funds for the technical aspects of the web site

Reason: All that I'm seeing so far is trucks, forklifts and planes. We are a legal mergers and acquisitions firm that focus on logistics. I like some of the images to say logistics, but really want it say legal, financial, and putting companies together. Will pay extra for the sub page if someone can impress us with a home page.

Reason: Swamped with another project at the moment...will work on this over the weekend and provide designer feedback and select final design by Tuesday

```html
<!DOCTYPE html>
<html lang="en">
<head>
<meta charset="utf-8">
<title>KVR Associates — Home</title>
<link rel="stylesheet" href="https://fonts.googleapis.com/css2?family=Rajdhani:wght@500;600&family=Ubuntu:wght@400;500;700&display=swap">
<style>
:root{
  --burgundy:#a6093a;
  --grey:#5a5a5c;
  --grey-dark:#2e2e30;
  --text:#3c3c3c;
  --page:#f2f2f2;
  --white:#ffffff;
  --hero-deep:#0b4f86;
  --hero-light:#29b7e6;
  --hero-glow:#9ff0ff;
}
*{box-sizing:border-box;margin:0;padding:0}
html,body{width:1028px;height:1200px;overflow:hidden}
body{position:relative;background:var(--page);font-family:"Ubuntu",sans-serif;color:var(--text)}

/* header */
.site-header{position:absolute;left:0;top:0;width:1028px;height:126px;background:linear-gradient(#f7f7f7,#e3e3e3);border-top:6px solid #6b6b6b}
.brand{position:absolute;left:120px;top:52px;display:flex;align-items:center;gap:10px}
.brand-mark{width:14px;height:14px;background:var(--burgundy)}
.brand-name{font-weight:500;font-size:25px;color:var(--grey);letter-spacing:.5px}
.social-top{position:absolute;left:648px;top:24px;display:flex;gap:12px}
.social-top span{width:28px;height:28px;border-radius:50%;background:radial-gradient(circle at 40% 35%,#777,#2b2b2b)}
.call{position:absolute;left:778px;top:20px;display:flex;align-items:center;gap:6px}
.call-text small{display:block;font-size:10px;color:#444}
.call-text strong{display:block;font-weight:400;font-size:16px;color:#333}
.main-nav{position:absolute;left:380px;top:75px;display:flex;gap:14px}
.main-nav a{display:block;font-size:9.5px;color:#333;text-decoration:none;padding:8px 9px;border-top:1px solid #bbb;border-bottom:1px solid #bbb;letter-spacing:.2px}
.main-nav a.active{font-weight:700;position:relative}
.main-nav a.active::before{content:"";position:absolute;left:50%;top:-1px;margin-left:-4px;border:4px solid transparent;border-top-color:#333}

/* hero */
.hero{position:absolute;left:0;top:126px;width:1028px;height:375px;overflow:hidden;background:radial-gradient(ellipse at 55% 30%,var(--hero-light) 0%,#1479b9 40%,var(--hero-deep) 100%)}
.hero-photo{position:absolute;inset:0;background:
  radial-gradient(ellipse 120px 220px at 370px 240px,rgba(235,240,248,.55),transparent 70%),
  radial-gradient(circle 110px at 730px 300px,rgba(120,220,255,.45),transparent 70%),
  radial-gradient(ellipse 200px 90px at 130px 110px,rgba(90,210,255,.35),transparent 70%)}
.hero-arrow{position:absolute;top:170px}
.hero-brand{position:absolute;left:458px;top:84px;font-family:"Ubuntu",sans-serif;font-weight:500;font-size:30px;letter-spacing:3px;color:#c9ecf7}
.hero-tag{position:absolute;left:568px;top:92px;width:170px;height:25px;border:2px solid var(--hero-glow);border-radius:3px;display:flex;align-items:center;gap:8px;padding-left:6px;font-family:"Rajdhani",sans-serif;font-weight:500;font-size:15px;letter-spacing:1px;color:var(--hero-glow)}
.hero-tag i{width:0;height:0;border-left:7px solid var(--hero-glow);border-top:4.5px solid transparent;border-bottom:4.5px solid transparent;margin-right:4px}
.hero-tag::before{content:"";position:absolute;left:22px;top:2px;bottom:2px;width:1.5px;background:var(--hero-glow)}
.hero-status{position:absolute;left:806px;top:356px;font-family:"Rajdhani",sans-serif;font-weight:500;font-size:10px;letter-spacing:.8px;color:#4fa9d8}

/* services */
.section-title{position:absolute;left:0;top:516px;width:1028px;text-align:center;font-family:"Rajdhani",sans-serif;font-weight:500;font-size:28px;color:var(--burgundy)}
.title-rule{position:absolute;top:530px;height:1px;width:222px;background:linear-gradient(90deg,transparent,#9a9a9a)}
.title-rule.right{background:linear-gradient(90deg,#9a9a9a,transparent)}
.service{position:absolute;top:563px;width:237px;height:148px;background:var(--white);box-shadow:0 1px 3px rgba(0,0,0,.2)}
.service-head{height:91px;background:var(--grey);position:relative}
.service-head.featured{background:var(--burgundy)}
.service-head h3{position:absolute;left:11px;bottom:5px;font-family:"Rajdhani",sans-serif;font-weight:500;font-size:21px;line-height:23px;color:var(--white)}
.service-head svg{position:absolute;right:8px;bottom:0}
.service p{padding:4px 9px;font-size:10.2px;line-height:14.5px;color:#444}
.divider-shadow{position:absolute;left:0;top:724px;width:1028px;height:16px;background:radial-gradient(ellipse at 50% 0%,rgba(0,0,0,.12),transparent 70%)}

/* panels */
.panel{position:absolute;top:760px;width:252px;height:233px;background:linear-gradient(#fafafa,#efefef);border-radius:6px;box-shadow:0 6px 6px -4px rgba(0,0,0,.25)}
.panel-head{position:absolute;left:-4px;right:-4px;top:11px;height:32px;background:var(--grey);display:flex;align-items:center;gap:10px;padding-left:12px;color:var(--white);font-size:16px;font-weight:400;letter-spacing:.6px}
.about-photo{position:absolute;left:8px;top:59px;width:228px;height:88px;background:linear-gradient(100deg,#e3e6ea,#9aa4b0 45%,#2a3646)}
.about-text{position:absolute;left:14px;top:153px;width:222px;font-size:9.3px;line-height:12.2px;letter-spacing:.4px;color:#444;text-align:justify}
.read-more{position:absolute;right:10px;bottom:12px;font-size:9.5px;font-weight:500;color:#333}
.news-item{position:absolute;left:10px;display:flex;gap:9px}
.date{width:31px;height:32px;text-align:center;box-shadow:0 1px 2px rgba(0,0,0,.25);background:var(--white)}
.date b{display:block;background:var(--burgundy);color:var(--white);font-size:10.5px;font-weight:500;padding:1px 0}
.date i{display:block;font-style:normal;font-size:9.5px;font-weight:700;padding:2px 0}
.news-item p{font-size:9.5px;line-height:12.2px;width:186px;color:#444}
.news-item strong{color:#222}
.field{position:absolute;left:12px;width:226px;height:21px;background:var(--white);border:1px solid #bdbdbd;border-radius:2px;font-size:10px;color:#555;padding:4px 8px}
.submit{position:absolute;left:14px;top:201px;width:55px;height:19px;background:var(--burgundy);color:var(--white);font-size:11.5px;font-weight:700;text-align:center;line-height:19px}

/* footer */
.site-footer{position:absolute;left:0;top:1017px;width:1028px;height:183px;background:var(--grey-dark);border-top:4px solid var(--burgundy)}
.footer-h{position:absolute;font-size:15px;font-weight:400;color:var(--white);padding-bottom:6px;border-bottom:1px dotted #666}
.quick-links{position:absolute;left:119px;top:47px;list-style:none}
.quick-links li{font-size:10px;color:var(--white);line-height:14.3px;padding-left:12px;position:relative}
.quick-links li::before{content:"›";position:absolute;left:0;color:#bbb}
.vrule{position:absolute;top:20px;width:1px;height:110px;background:#555}
.map{position:absolute;left:288px;top:47px;width:185px;height:81px;background:linear-gradient(135deg,#efece6,#dcd8cf)}
.contact-row{position:absolute;left:480px;display:flex;gap:8px;align-items:flex-start;font-size:10px;line-height:15px;color:var(--white)}
.footer-brand{position:absolute;left:730px;top:16px;width:178px;text-align:center;font-weight:500;font-size:52px;letter-spacing:6px;color:var(--white)}
.social-foot{position:absolute;left:765px;top:95px;display:flex;gap:10px}
.social-foot span{width:31px;height:31px;border-radius:50%;background:#6a6a6a;box-shadow:0 2px 2px rgba(0,0,0,.4)}
.copyright{position:absolute;left:0;top:153px;width:1028px;text-align:center;font-size:12px;color:var(--white)}
</style>
</head>
<body>

<header class="site-header">
  <div class="brand"><span class="brand-mark"></span><span class="brand-name">KVR Associates</span></div>
  <div class="social-top" aria-label="Social links"><span></span><span></span><span></span></div>
  <div class="call">
    <svg width="28" height="28" viewBox="0 0 28 28"><circle cx="14" cy="14" r="12.5" fill="none" stroke="#a6093a" stroke-width="1.6"/><path d="M10 8c-2 2-1 7 3 11s8 5 9 3l-3-3-2 1c-2-1-4-3-5-5l1-2z" fill="#a6093a"/></svg>
    <div class="call-text"><small>Call Us Today</small><strong>555 014 2290</strong></div>
  </div>
  <nav class="main-nav">
    <a class="active" href="#">HOME</a>
    <a href="#">ABOUT US</a>
    <a href="#">BUYER SERVICES</a>
    <a href="#">SELLER SERVICES</a>
    <a href="#">NEWS &amp; EVENTS</a>
    <a href="#">FAQ's</a>
    <a href="#">CONTACT</a>
  </nav>
</header>

<section class="hero">
  <div class="hero-photo" role="img" aria-label="Hero photograph: a professional woman touching a glowing digital interface over a blue world map, bar chart and globe"></div>
  <div class="hero-brand">KVR</div>
  <div class="hero-tag"><i></i>Business solutions</div>
  <div class="hero-status">Loaded 100%</div>
  <svg class="hero-arrow" style="left:96px" width="24" height="34" viewBox="0 0 24 34"><path d="M18 3L5 17l13 14" fill="none" stroke="#fff" stroke-width="4"/></svg>
  <svg class="hero-arrow" style="left:908px" width="24" height="34" viewBox="0 0 24 34"><path d="M6 3l13 14L6 31" fill="none" stroke="#fff" stroke-width="4"/></svg>
</section>

<div class="title-rule" style="left:200px"></div>
<h2 class="section-title">Our Services</h2>
<div class="title-rule right" style="left:616px"></div>

<article class="service" style="left:119px">
  <div class="service-head featured">
    <h3>Business<br>Planning</h3>
    <svg width="60" height="62" viewBox="0 0 60 62"><rect x="8" y="2" width="44" height="58" rx="3" fill="none" stroke="#fff" stroke-width="3"/><path d="M16 14h28M16 22h28M16 30h28M16 38h18" stroke="#fff" stroke-width="3"/><path d="M30 46l8 8 18-20" fill="none" stroke="#fff" stroke-width="4"/></svg>
  </div>
  <p>Lorem ipsum dolor sit amet, consectetuer eadi pis elit, sed diam nonummy nibh euismod tinc idunt ut laoreeio dolore magna aliquam erate</p>
</article>
<article class="service" style="left:394px">
  <div class="service-head">
    <h3>Mergers &amp;<br>Acquisition</h3>
    <svg width="70" height="50" viewBox="0 0 70 50"><circle cx="25" cy="25" r="15" fill="none" stroke="#fff" stroke-width="5"/><circle cx="45" cy="25" r="15" fill="none" stroke="#fff" stroke-width="5"/></svg>
  </div>
  <p>Lorem ipsum dolor sit amet, consectetuer eadi pis elit, sed diam nonummy nibh euismod tinc idunt ut laoreeio dolore magna aliquam erate</p>
</article>
<article class="service" style="left:670px">
  <div class="service-head">
    <h3>Advisory<br>Services</h3>
    <svg width="54" height="62" viewBox="0 0 54 62"><circle cx="18" cy="34" r="8" fill="#fff"/><path d="M2 60c0-12 7-16 16-16s16 4 16 16z" fill="#fff"/><rect x="24" y="4" width="28" height="20" rx="3" fill="none" stroke="#fff" stroke-width="2.5"/><path d="M30 24l-4 6 8-6M29 11h18M29 17h14" stroke="#fff" stroke-width="2.5" fill="none"/></svg>
  </div>
  <p>Lorem ipsum dolor sit amet, consectetuer eadi pis elit, sed diam nonummy nibh euismod tinc idunt ut laoreeio dolore magna aliquam erate</p>
</article>

<div class="divider-shadow"></div>

<section class="panel" style="left:123px">
  <h3 class="panel-head">
    <svg width="20" height="16" viewBox="0 0 20 16"><circle cx="10" cy="4" r="3" fill="#fff"/><circle cx="4" cy="6" r="2.5" fill="#fff"/><circle cx="16" cy="6" r="2.5" fill="#fff"/><path d="M5 15c0-5 2-7 5-7s5 2 5 7zM0 14c0-4 1-5 4-5l1 5zM20 14c0-4-1-5-4-5l-1 5z" fill="#fff"/></svg>
    ABOUT KVR
  </h3>
  <div class="about-photo" role="img" aria-label="Photograph of three business colleagues in conversation"></div>
  <p class="about-text">KVR assists business owners within the logistics industry to implement growth and exit strategies. We offer business planning and merger and acquisition (M&amp;A) advisory services.</p>
  <span class="read-more">Read More »</span>
</section>

<section class="panel" style="left:394px">
  <h3 class="panel-head">
    <svg width="17" height="17" viewBox="0 0 17 17"><rect x="1" y="3" width="15" height="13" fill="none" stroke="#fff" stroke-width="1.5"/><path d="M1 6h15M4 1v4M13 1v4" stroke="#fff" stroke-width="1.5"/><path d="M4 9h2M8 9h2M12 9h2M4 12h2M8 12h2M12 12h2" stroke="#fff" stroke-width="1.5"/></svg>
    NEWS &amp; EVENTS
  </h3>
  <div class="news-item" style="top:59px"><div class="date"><b>Apr</b><i>02</i></div><p><strong>Lorem ipsum dolor sit amet, consectetue</strong> eadi pis elit, sed diam nonummy nibherini euismod tinc idunt ut laoreeio.</p></div>
  <div class="news-item" style="top:107px"><div class="date"><b>Apr</b><i>03</i></div><p><strong>Lorem ipsum dolor sit amet, consectetue</strong> eadi pis elit, sed diam nonummy nibherini euismod tinc idunt ut laoreeio.</p></div>
  <div class="news-item" style="top:155px"><div class="date"><b>Apr</b><i>04</i></div><p><strong>Lorem ipsum dolor sit amet, consectetue</strong> eadi pis elit, sed diam nonummy nibherini euismod tinc idunt ut laoreeio.</p></div>
  <span class="read-more">Read More »</span>
</section>

<section class="panel" style="left:664px">
  <h3 class="panel-head">
    <svg width="17" height="18" viewBox="0 0 17 18"><path d="M12 2H2v15h11v-5" fill="none" stroke="#fff" stroke-width="1.6"/><path d="M7 12l1-3 7-7 2 2-7 7z" fill="#fff"/></svg>
    QUICK CONTACT
  </h3>
  <div class="field" style="top:59px">Name</div>
  <div class="field" style="top:88px">Email</div>
  <div class="field" style="top:116px">Phone</div>
  <div class="field" style="top:144px;height:53px">Message</div>
  <div class="submit">Submit</div>
</section>

<footer class="site-footer">
  <h4 class="footer-h" style="left:119px;top:18px;width:104px">Quick Links</h4>
  <ul class="quick-links">
    <li>Home</li><li>About Us</li><li>Consulting Services</li><li>News &amp; Events</li><li>FAQ's</li><li>Contact Us</li>
  </ul>
  <div class="vrule" style="left:255px"></div>
  <h4 class="footer-h" style="left:288px;top:18px;width:376px">Contact Us</h4>
  <div class="map" role="img" aria-label="Street map showing the office location"></div>
  <div class="contact-row" style="top:50px">
    <svg width="16" height="16" viewBox="0 0 16 16"><path d="M1 8L8 2l7 6M3 7v8h4v-4h2v4h4V7" fill="#fff"/></svg>
    <span>Lorem ipsum dolor sit amet, conse<br>adipiscing elit, sed diam nonummy.</span>
  </div>
  <div class="contact-row" style="top:89px">
    <svg width="16" height="16" viewBox="0 0 16 16"><circle cx="8" cy="8" r="7" fill="none" stroke="#fff" stroke-width="1.3"/><path d="M6 4c-1 1-1 4 1 6s4 3 5 2l-1.5-1.5-1 .5c-1-.5-2-1.5-2.5-2.5l.5-1z" fill="#fff"/></svg>
    <span>555.014.2290</span>
  </div>
  <div class="contact-row" style="top:115px">
    <svg width="16" height="16" viewBox="0 0 16 16"><circle cx="8" cy="8" r="3" fill="none" stroke="#fff" stroke-width="1.6"/><path d="M11 5v4c0 2 3 2 3-1a6 6 0 1 0-3 5" fill="none" stroke="#fff" stroke-width="1.6"/></svg>
    <span>info@kvrassociates-example.com</span>
  </div>
  <div class="vrule" style="left:700px"></div>
  <div class="footer-brand">KVR</div>
  <div class="social-foot" aria-label="Social links"><span></span><span></span><span></span></div>
  <p class="copyright">© 2014 kvrassociates-example.&nbsp; All Rights Reserved .</p>
</footer>

</body>
</html>
```